Crest of Morning Paddocks Business Cards with logo

Need a creative business card that pops. Colorful but professional. The attached logo should be included. We are a national horse racing partnership so we are in the equine business. Nothing cartoonlike or whimsical.

Target Market(s)

professionals - 40+

Contact Information for Business Card

Maren Dunleavy
Director of Operations
27 Ashbrook Lane
Middletown, MD. 21584

Phone (313) 555-0147

FX: (949) 555-0192

email: maren@cmpaddocks.example
cmpaddocks.example

Requirements
Must have
• All information above should be on the business card including the website address. Professional yet creative
Nice to have
• an attention grabbing design. not boring. exciting.
Should not have
• cartoon like - whimsical.

```html
<!DOCTYPE html>
<html lang="en">
<head>
<meta charset="utf-8">
<title>Crest of Morning Paddocks – Business Card</title>
<link href="https://fonts.googleapis.com/css2?family=Cinzel:wght@400;600&family=Tinos&family=Roboto:wght@400&display=swap" rel="stylesheet">
<style>
  :root {
    --navy: #2f3673;
    --navy-light: #3e4680;
    --gold: #c9a43d;
    --ink: #4a4a4a;
    --paper: #ffffff;
    --backdrop: #e4e4e4;
  }
  * { box-sizing: border-box; margin: 0; padding: 0; }
  html, body { width: 1200px; height: 1200px; overflow: hidden; }
  body { background: var(--backdrop); position: relative; }

  .card {
    position: absolute;
    left: 200px;
    width: 800px;
    height: 457px;
    overflow: hidden;
  }
  .card--front { top: 150px; background: var(--paper); }
  .card--back {
    top: 640px;
    background: linear-gradient(180deg, var(--navy-light) 0%, var(--navy) 100%);
  }

  .band { position: absolute; left: 136px; width: 110px; }
  .band--gold { top: 0; height: 140px; background: var(--gold); }
  .band--navy { top: 300px; bottom: 0; background: var(--navy); }

  .crest {
    position: absolute;
    left: 64px; top: 98px;
    width: 252px; height: 252px;
    border-radius: 50%;
    background: var(--paper);
    display: flex; align-items: center; justify-content: center;
  }
  .crest-ring {
    position: absolute;
    inset: 28px;
    border-radius: 50%;
    border: 1.5px solid var(--gold);
  }
  .crest-name {
    font-family: "Cinzel", serif;
    font-weight: 600;
    font-size: 21px;
    line-height: 1.25;
    color: var(--navy);
    text-align: center;
    letter-spacing: 1px;
  }

  .details { position: absolute; left: 372px; top: 100px; }
  .person-name {
    font-family: "Cinzel", serif;
    font-weight: 600;
    font-size: 30px;
    color: var(--navy);
    line-height: 1;
    letter-spacing: 0.5px;
  }
  .person-title {
    font-family: "Cinzel", serif;
    font-weight: 400;
    font-size: 20px;
    color: var(--gold);
    letter-spacing: 1.2px;
    margin-top: 4px;
  }
  .address {
    font-family: "Tinos", serif;
    font-size: 19px;
    color: var(--ink);
    line-height: 24px;
    margin-top: 30px;
    font-style: normal;
  }
  .contacts { list-style: none; margin-top: 13px; }
  .contacts li {
    font-family: "Tinos", serif;
    font-size: 19px;
    color: var(--ink);
    line-height: 25.5px;
    display: flex; align-items: center;
  }
  .contacts svg { width: 18px; height: 18px; margin-right: 12px; fill: var(--navy); flex: none; }

  .back-name {
    position: absolute;
    left: 0; right: 0; top: 150px;
    text-align: center;
    font-family: "Cinzel", serif;
    font-weight: 600;
    font-size: 40px;
    line-height: 1.25;
    color: var(--paper);
    letter-spacing: 2px;
  }
  .back-url {
    position: absolute;
    left: 0; right: 0; top: 398px;
    text-align: center;
    font-family: "Roboto", sans-serif;
    font-size: 19px;
    color: var(--paper);
    letter-spacing: 7px;
  }
</style>
</head>
<body>
  <section class="card card--front">
    <div class="band band--gold"></div>
    <div class="band band--navy"></div>
    <div class="crest">
      <div class="crest-ring"></div>
      <div class="crest-name">Crest of<br>Morning<br>Paddocks</div>
    </div>

    <div class="details">
      <h1 class="person-name">Maren Dunleavy</h1>
      <p class="person-title">Director of Operations</p>
      <address class="address">27 Ashbrook Lane<br>Middletown, MD. 21584</address>
      <ul class="contacts">
        <li><svg viewBox="0 0 24 24"><path d="M6.6 10.8a15.1 15.1 0 0 0 6.6 6.6l2.2-2.2a1 1 0 0 1 1-.25 11.4 11.4 0 0 0 3.6.57 1 1 0 0 1 1 1V20a1 1 0 0 1-1 1A17 17 0 0 1 3 4a1 1 0 0 1 1-1h3.5a1 1 0 0 1 1 1c0 1.25.2 2.45.57 3.57a1 1 0 0 1-.25 1z"/></svg>(313) 555-0147</li>
        <li><svg viewBox="0 0 24 24"><path d="M7 3h10v5H7zM3 9h18v9h-3v3H6v-3H3zm5 6v4h8v-4z"/></svg>(949) 555-0192</li>
        <li><svg viewBox="0 0 24 24"><path d="M2 5h20v14H2zm2 2v.5l8 5.5 8-5.5V7zm0 3v7h16v-7l-8 5.5z"/></svg>maren@cmpaddocks.example</li>
        <li><svg viewBox="0 0 24 24"><path d="M12 2a10 10 0 1 0 0 20 10 10 0 0 0 0-20zm-1 17.9A8 8 0 0 1 4.2 10.5L9 15v1a2 2 0 0 0 2 2zm6.9-2.5A2 2 0 0 0 16 16h-1v-3a1 1 0 0 0-1-1H8v-2h2a1 1 0 0 0 1-1V7h2a2 2 0 0 0 2-2v-.4a8 8 0 0 1 2.9 12.8z"/></svg>www.cmpaddocks.example</li>
      </ul>
    </div>
  </section>

  <section class="card card--back">
    <div class="back-name">Crest of<br>Morning Paddocks</div>
    <p class="back-url">www.cmpaddocks.example</p>
  </section>
</body>
</html>
```